Poster to advertise new mind coaching clinic

Create a single sided A4 colour poster using the text provided. Suggested image provided. You may want to suggest an alternative however images need to appeal to both male and female sports people.

Text:
One-to-one mind coaching
For recreational and competitive sports people
Learn the mental tools and techniques used by the top sports people to fulfil your potential

 Create well-formed and achievable goals
 Overcome limiting beliefs
 Accelerate mastery through modelling your heroes
 Learn how to use mental rehearsal to increase your chances of success
 Smash through belief ceilings
 Get into the zone to bring your ‘A-Game’ more often
Thursdays in central Twyford
5-8pm
For more information contact:
thebluekitecoaching@postmere.com
Tel: 07481 265314
www.the-blue-kite.co.uk

Target Market(s)

sports people

Industry/Entity Type

Clinic

Requirements
Must have
• All the content provided. Contact details.

```html
<!DOCTYPE html>
<html lang="en">
<head>
<meta charset="UTF-8">
<title>One-to-One Mind Coaching Poster</title>
<link rel="stylesheet" href="https://fonts.googleapis.com/css2?family=Anton&family=Open+Sans:wght@400;600;700;800&display=swap">
<style>
  :root {
    --navy: #0d1b4d;
    --royal: #1d4fc4;
    --sky: #2fa3e6;
    --violet: #6b2fb8;
    --orange: #f28a1c;
    --pink: #e8356f;
    --green: #3cbf5a;
    --yellow: #ffe600;
    --white: #ffffff;
    --ink: #111111;
  }
  * { margin: 0; padding: 0; box-sizing: border-box; }
  html, body { width: 849px; height: 1200px; overflow: hidden; background: var(--white); }
  .poster {
    position: relative;
    width: 849px;
    height: 1200px;
    overflow: hidden;
    font-family: "Open Sans", Arial, sans-serif;
    background: var(--navy);
  }
  .geometric-backdrop {
    position: absolute;
    left: 0; top: 0;
    width: 849px; height: 840px;
    background:
      linear-gradient(125deg, rgba(47,163,230,0.0) 40%, rgba(242,138,28,0.55) 62%, rgba(232,53,111,0.5) 75%, rgba(60,191,90,0.45) 92%),
      linear-gradient(200deg, var(--sky) 0%, var(--royal) 35%, var(--violet) 70%, var(--royal) 100%);
  }
  .athlete-photo {
    position: absolute;
    left: 110px; top: 235px;
    width: 545px; height: 605px;
    background: radial-gradient(ellipse at 50% 40%, #8a5a48 0%, #5a3a34 30%, #1f2c66 65%, rgba(29,79,196,0) 80%);
  }
  .headline {
    position: absolute;
    top: 40px; left: 0; width: 100%;
    text-align: center;
    color: var(--white);
    font-family: "Anton", "Impact", sans-serif;
    text-transform: uppercase;
    line-height: 0.98;
    text-shadow: 0 3px 6px rgba(0,0,0,0.35);
  }
  .headline .line-one,
  .headline .line-two { display: block; font-size: 84px; letter-spacing: 1px; }
  .subtitle {
    position: absolute;
    top: 210px; left: 0; width: 100%;
    text-align: center;
    color: var(--white);
    font-weight: 800;
    font-size: 22px;
    text-transform: uppercase;
    letter-spacing: 0.5px;
  }
  .promise-banner {
    position: absolute;
    left: 60px; top: 470px;
    width: 440px; height: 150px;
    background: var(--yellow);
    transform: rotate(-10deg);
    display: flex; align-items: center;
    padding: 0 24px 0 44px;
    color: var(--ink);
    font-weight: 800;
    font-size: 21px;
    line-height: 1.25;
    box-shadow: 0 4px 10px rgba(0,0,0,0.3);
  }
  .contact-card {
    position: absolute;
    left: 540px; top: 365px;
    width: 285px; height: 225px;
    background: var(--yellow);
    transform: rotate(-9deg);
    padding: 30px 14px 18px 22px;
    color: var(--ink);
    font-size: 15px;
    line-height: 1.45;
    box-shadow: 0 4px 10px rgba(0,0,0,0.3);
  }
  .contact-card .venue { font-weight: 800; font-size: 18px; margin-bottom: 2px; }
  .contact-card .email { font-size: 13.5px; white-space: nowrap; }
  .benefits {
    position: absolute;
    left: 40px; top: 878px;
    width: 540px;
    list-style: none;
    color: var(--white);
    font-size: 18.5px;
    line-height: 1.32;
  }
  .benefits li {
    position: relative;
    padding-left: 22px;
    margin-bottom: 12px;
  }
  .benefits li::before {
    content: "";
    position: absolute;
    left: 2px; top: 10px;
    width: 6px; height: 6px;
    border-radius: 50%;
    background: var(--white);
  }
  .brand-panel {
    position: absolute;
    left: 608px; top: 878px;
    width: 241px; height: 255px;
    background: var(--white);
    display: flex; align-items: center; justify-content: center;
    gap: 10px;
    padding: 0 12px;
  }
  .brand-panel .brand-dot {
    width: 20px; height: 20px;
    border-radius: 50%;
    background: var(--royal);
    flex: none;
  }
  .brand-panel .brand-name {
    font-family: "Open Sans", Arial, sans-serif;
    font-weight: 800;
    font-size: 24px;
    line-height: 1.1;
    white-space: nowrap;
    color: var(--navy);
  }
</style>
</head>
<body>
  <main class="poster">
    <div class="geometric-backdrop" role="img" aria-label="Colourful abstract backdrop of angular blue, purple, orange, pink and green shapes"></div>
    <div class="athlete-photo" role="img" aria-label="Photo of a sprinter celebrating with arms outstretched, holding a relay baton"></div>

    <h1 class="headline">
      <span class="line-one">One-to-One</span>
      <span class="line-two">Mind Coaching</span>
    </h1>
    <p class="subtitle">For recreational and competitive sports people</p>

    <p class="promise-banner">Learn the mental tools and techniques used by the top sports people to fulfil your potential</p>

    <div class="contact-card">
      <p class="venue">In Central Twyford</p>
      <p>Thursdays 5-8pm</p>
      <p>For more Information Contact:</p>
      <p class="email">thebluekitecoaching@postmere.com</p>
      <p>Tel: 07481 265314</p>
      <p>www.the-blue-kite.co.uk</p>
    </div>

    <ul class="benefits">
      <li>Create well-formed and achievable goals</li>
      <li>Overcome limiting beliefs</li>
      <li>Accelerate mastery through modelling your heroes</li>
      <li>Learn how to use mental rehearsal to increase your Chances of success</li>
      <li>Smash through belief ceilings</li>
      <li>Get into the zone to bring your ‘A-Game’ more often</li>
    </ul>

    <div class="brand-panel">
      <span class="brand-dot"></span>
      <span class="brand-name">The Blue Kite</span>
    </div>
  </main>
</body>
</html>
```